Innovative approaches to treat addiction

PowerPoint on different techniques
Add graphics to screen
Easy to follow
I've provided the PowerPoint w content
Now make it pretty
And
hand outs for them to follow and take notes
Can you also add my bio:
Mara J. Thornquist, MS LCADC is a licensed Psychotherapist with a specialty in Addiction Disorders and over 22 years of clinical experience. Her integrative approach to counseling combines years of clinical experience with cognitive behavioral and traditional psychotherapy, with holistic therapies including; mindfulness, NLP, hypnotherapy, yoga therapy, reiki, motivational and wellness coaching.
Handout materials for them to follow and take notes

```html
<!DOCTYPE html>
<html lang="en">
<head>
<meta charset="utf-8">
<title>Innovative Techniques to Treat Disorders</title>
<link rel="stylesheet" href="https://fonts.googleapis.com/css2?family=Montserrat:wght@300;400;600;800&display=swap">
<style>
  :root {
    --page: #f7f7f7;
    --navy: #0f1b28;
    --navy-soft: #1c2b3b;
    --blue: #5b9bd6;
    --blue-light: #a9cbee;
    --blue-deep: #1f5d93;
    --ink-dark: #24364d;
    --orange: #f4714b;
    --orange-strong: #fb5117;
    --coral: #ec4f4b;
    --dot: #f15c3b;
    --dot-ring: #fde1d8;
    --grey-text: #6a6a6a;
    --rule: #e2e2e2;
    --white: #ffffff;
  }
  * { box-sizing: border-box; margin: 0; padding: 0; }
  html, body { width: 719px; height: 1200px; overflow: hidden; }
  body {
    background: var(--page);
    font-family: "Montserrat", Arial, sans-serif;
    position: relative;
  }
  .slide {
    position: absolute;
    left: 37px;
    width: 650px;
    height: 366px;
    overflow: hidden;
    box-shadow: 0 4px 14px rgba(0,0,0,0.18);
  }
  .abs { position: absolute; }

  /* Title slide */
  .slide--title { top: 30px; background: var(--navy); }
  .title-art {
    inset: 0;
    background: radial-gradient(ellipse at 50% 60%, var(--navy-soft) 0%, var(--navy) 75%);
  }
  .title-block { left: 0; right: 0; top: 132px; text-align: center; color: var(--white); }
  .title-block h1 { font-weight: 800; font-size: 24px; line-height: 30px; letter-spacing: 0.2px; }
  .title-block .presenter { margin-top: 9px; font-size: 11.5px; font-weight: 400; }

  /* Approaches overview */
  .slide--overview { top: 412px; background: var(--blue); }
  .overview-heading {
    left: 27px; top: 14px; color: var(--white);
    font-weight: 800; font-size: 21.5px; line-height: 29px;
  }
  .outcome-list {
    left: 27px; top: 83px; list-style: none; color: var(--white);
    font-size: 11.3px; line-height: 14.7px; font-weight: 400; width: 270px;
  }
  .outcome-list li { position: relative; padding-left: 15px; }
  .outcome-list li::before { content: "•"; position: absolute; left: 0; }
  .callout { left: 30px; top: 210px; }
  .callout-text {
    left: 53px; top: 266px; width: 240px;
    font-size: 8.3px; line-height: 11.4px; color: var(--ink-dark); font-weight: 400;
  }
  .clinic-art {
    left: 367px; top: 52px; width: 283px; height: 314px;
    background: linear-gradient(160deg, #e9eff5 0%, #cfdbe8 45%, var(--blue-deep) 100%);
    border-radius: 40px 0 0 0;
  }

  /* Approaches list */
  .slide--methods { top: 798px; background: var(--white); }
  .methods-panel { left: 0; top: 0; width: 252px; height: 366px; background: var(--orange); }
  .lab-art {
    left: 18px; top: 64px; width: 232px; height: 232px; border-radius: 50%;
    background: radial-gradient(circle at 55% 45%, #fbe9e4 0%, #f6a892 50%, var(--orange) 78%);
  }
  .methods-bar {
    left: 217px; top: 18px; width: 406px; height: 30px; background: var(--orange-strong);
    color: var(--white); font-weight: 600; font-size: 12.5px; line-height: 30px; padding-left: 19px;
  }
  .method { width: 120px; text-align: center; transform: translateX(-50%); }
  .badge {
    width: 27px; height: 27px; margin: 0 auto; border-radius: 50%;
    background: var(--dot); border: 2px solid var(--dot-ring);
    color: var(--white); font-weight: 600; font-size: 10.5px; line-height: 23px; text-align: center;
  }
  .method-label { margin-top: 6px; font-size: 11.3px; line-height: 14.5px; color: var(--grey-text); font-weight: 400; }
  .rule-v { width: 1px; background: var(--rule); }
  .rule-h { height: 1px; background: var(--rule); }
  .nlp-bar {
    left: 291px; top: 220px; width: 332px; height: 27px; background: var(--coral);
    color: var(--white); font-size: 11.3px; line-height: 27px; text-align: center; font-weight: 400;
  }
</style>
</head>
<body>

<section class="slide slide--title">
  <div class="abs title-art" role="img" aria-label="Faint medical illustration: two human silhouettes holding hands surrounded by healthcare icons, heart monitor, ambulance, pills and lab tubes on a chart grid"></div>
  <div class="abs title-block">
    <h1>Innovative Techniques to<br>Treat Disorders</h1>
    <p class="presenter">Mara J. Thornquist, MS LCADC, CHT, 500RYT</p>
  </div>
</section>

<section class="slide slide--overview">
  <h2 class="abs overview-heading">New Innovative Approaches<br>for Treatment of Addiction</h2>
  <ul class="abs outcome-list">
    <li>In the next hour you will learn tools that:</li>
    <li>Increase patient retention</li>
    <li>Increase rapport</li>
    <li>Increase healing time</li>
    <li>Increase compliance with treatment recommendations</li>
    <li>Reduce stress</li>
    <li>Reduce burnout</li>
    <li>Fun and sustainable</li>
    <li>Anyone can do it!</li>
  </ul>
  <svg class="abs callout" width="280" height="140" viewBox="0 0 280 140" aria-hidden="true">
    <path d="M13 38 H233 L274 6 L258 38 H276 Q279 38 279 41 V134 Q279 137 276 137 H16 Q13 137 13 134 Z" fill="var(--blue-light)" opacity="0.85"/>
    <path d="M7 29 h6 v-6 h6 v6 h6 v6 h-6 v6 h-6 v-6 h-6 z" fill="none" stroke="var(--blue-light)" stroke-width="1.6"/>
  </svg>
  <p class="abs callout-text">These techniques are not a replacement of standard medical procedures, but works in conjunction with them by freeing the patient of feelings or attitudes that may be compromising his or her natural immune system.</p>
  <div class="abs clinic-art" role="img" aria-label="Illustration of a doctor with a stethoscope showing a heart monitor to a patient seated in an exam chair"></div>
</section>

<section class="slide slide--methods">
  <div class="abs methods-panel">
    <div class="abs lab-art" role="img" aria-label="Illustration of a lab flask with red liquid, a test tube, a dropper and a medical prescription sheet"></div>
  </div>
  <div class="abs methods-bar">The Innovative Approaches</div>

  <div class="abs rule-v" style="left:390px; top:74px; height:62px;"></div>
  <div class="abs rule-v" style="left:504px; top:74px; height:62px;"></div>
  <div class="abs rule-h" style="left:299px; top:136px; width:312px;"></div>
  <div class="abs rule-v" style="left:448px; top:136px; height:62px;"></div>

  <div class="abs method" style="left:331px; top:80px;"><div class="badge">1</div><p class="method-label">Mindfulness</p></div>
  <div class="abs method" style="left:446px; top:80px;"><div class="badge">2</div><p class="method-label">Meditation</p></div>
  <div class="abs method" style="left:560px; top:80px;"><div class="badge">3</div><p class="method-label">Breathwork</p></div>
  <div class="abs method" style="left:374px; top:145px; width:140px;"><div class="badge">4</div><p class="method-label" style="margin-top:9px;">Asana/ Hand Mudra</p></div>
  <div class="abs method" style="left:530px; top:145px; width:160px;"><div class="badge">5</div><p class="method-label" style="margin-top:9px;">Hypnosis/ Self Hypnosis</p></div>

  <div class="abs nlp-bar">Neuro-linguisitic Programming</div>

  <div class="abs method" style="left:334px; top:263px;"><div class="badge">a</div><p class="method-label">Rapport</p></div>
  <div class="abs method" style="left:458px; top:263px;"><div class="badge">b</div><p class="method-label">Five<br>representational<br>Systems</p></div>
  <div class="abs method" style="left:586px; top:263px;"><div class="badge">c</div><p class="method-label">Mirroring</p></div>
</section>

</body>
</html>
```